Product Labels for soaps lines

I have bar soap, liquid soap, lip balm, lotion bar, lotion and bath bomb ,I already have a logo and I need product labels for shape of Square, Circle, Rectangle and oval,

The design need to match my logo.

example of the texts:( rectangle)

Hair Shampoo

100% handmade - Sulfate Free

Ingredients: Canola Oil ,Ricinus Communis (Castor) Seed Oil ,Cocos Nucifera (Coconut) Oil ,Simmondsia Chinensis (Jojoba) Seed Oil ,Aqua ( Water),Potassium hydroxide ,Fragrance

NT WT 8 OZ

Rectangle label measurement : 2 *4 for liquid shampoo
rectangle-horizontal or oval : 2.5*2 for bar soap
Circle : 1.5 for lip balm and 2 ' for lotion bar
rectangle label : 2*3 for lotion
circle label: 2.3 for body butter
rectangle label :1*1.5 facial serum

example of the texts:( medium rectangle)

Natural Body Soap

Ricinus Communis (Castor) Seed Oil ,Cocos Nucifera (Coconut) Oil ,Hydrogenated Palm Oil ,Prunus Amygdalus Dulcis (Sweet Almond) Oil ,Butyrospermum Parkii (Shea Butter) Fruit ,Beeswax ,Oryza Sativa (Rice) Bran Oil ,Olea Europaea (Olive) Oil ,Aqua ( Water),Sodium hydroxide ,Raw Goat Milk,Mica,Fragrance
Approx. 5 OZ

hand Wash/Body Wash lable size 2*4
Ricinus Communis (Castor) Seed Oil ,Cocos Nucifera (Coconut) Oil ,Theobroma Cacao (Cocoa) Seed Butter ,Olea Europaea (Olive) Oil ,Oryza Sativa (Rice) Bran Oil ,Aqua ( Water),Potassium hydroxide ,Fragrance

Avacado Facial Wash lable size 2*4
Canola Oil ,Ricinus Communis (Castor) Seed Oil ,Cocos Nucifera (Coconut) Oil ,Persea Gratissima (Avocado) Oil ,Prunus Amygdalus Dulcis (Sweet Almond) Oil ,Oryza Sativa (Rice) Bran Oil ,Aqua ( Water),Potassium hydroxide ,Fragrance

Lotion Bar
Cocos Nucifera (Coconut) Oil ,Mangifera Indica (Mango) Seed Butter ,Butyrospermum Parkii (Shea Butter) Fruit ,Beewax

Body Butter
Cocos Nucifera (Coconut) Oil ,Butyrospermum Parkii (Shea Butter) Fruit ,Theobroma Cacao (Cocoa) Seed Butter ,Helianthus Annuus (Sunflower) Seed Oil

lip balm,
Olea Europaea (Olive) Oil ,Butyrospermum Parkii (Shea Butter) Fruit ,Vitis Vinifera (Grape) Seed Oil ,Beewax,Fragrance

facial serum:1*1.5
Prunus Armeniaca (Apricot) Kernel Oil ,Argania Spinosa (Argan) Nut Oil ,Simmondsia Chinensis (Jojoba) Seed Oil ,Rosa Canina Fruit Oil

Target Market(s)

Logo color can be changed to a little darker blue

Industry/Entity Type

Hair

Font styles to use
Serif

Colors
fece3e
f04a50
33b7a4
8869ae

Requirements
Must have

• company name " Soap brambleton " is inspired by Tobin of the Saltmarsh, fun and adventurous spirit, design need to be fun ..
Nice to have
• Fun, Simple and eye catching ..

```html
<!DOCTYPE html>
<html lang="en">
<head>
<meta charset="utf-8">
<title>Hair Shampoo – Label Sheet</title>
<link href="https://fonts.googleapis.com/css2?family=Griffy&family=Open+Sans&display=swap" rel="stylesheet">
<style>
  :root {
    --brown: #43200f;
    --navy: #050585;
    --plum: #5b1761;
    --title-teal: #1b8c90;
    --khaki: #dcdca6;
    --ink: #3a1a10;
    --foam-light: #fbfbee;
    --foam-mid: #e9e8c4;
    --foam-dark: #c7c38a;
    --frame: #555;
  }
  * { box-sizing: border-box; margin: 0; padding: 0; }
  html, body { width: 1200px; height: 1000px; overflow: hidden; background: #fff; }
  .sheet { position: relative; width: 1200px; height: 1000px; font-family: "Open Sans", sans-serif; }

  .sheet__title {
    position: absolute; top: 14px; left: 0; width: 100%;
    text-align: center; font-size: 30px; font-weight: 400; color: #000; letter-spacing: 0.5px;
  }

  .size-caption { position: absolute; width: 180px; text-align: center; font-size: 15px; color: #000; }

  .label {
    position: absolute; width: 180px; height: 360px;
    border: 1px solid var(--frame); background: #fff; overflow: hidden;
  }
  .label--short { height: 270px; }
  .label--brown { --label-color: var(--brown); }
  .label--navy { --label-color: var(--navy); }
  .label--plum { --label-color: var(--plum); }

  .label__top { position: relative; height: 125px; background: var(--label-color); }
  .label--short .label__top { height: 92px; }

  .brand {
    position: absolute; top: 42px; left: 0; width: 100%; text-align: center;
    font-family: "Griffy", cursive; font-weight: 400; font-size: 21px;
    color: var(--khaki); line-height: 1; white-space: nowrap;
  }
  .label--short .brand { top: 28px; }

  .foam {
    position: absolute;
    background: radial-gradient(ellipse at 40% 30%, var(--foam-light) 0%, var(--foam-mid) 55%, var(--foam-dark) 100%);
  }
  .foam--crest { left: 2px; right: 2px; bottom: -10px; height: 36px; border-radius: 18px 18px 6px 6px; z-index: 1; }
  .label--short .foam--crest { height: 30px; }
  .foam--base { bottom: 0; left: 20px; width: 140px; height: 40px; border-radius: 22px 22px 0 0; }
  .label--short .foam--base { left: auto; right: 6px; width: 48px; height: 22px; border-radius: 12px 12px 0 0; }

  .label__band { position: relative; height: 62px; background: var(--khaki); text-align: center; padding-top: 14px; }
  .label--short .label__band { height: 78px; padding-top: 28px; }
  .label__name { font-family: "Griffy", cursive; font-size: 19px; color: var(--title-teal); line-height: 1; }
  .label__claim { font-family: "Griffy", cursive; font-size: 10.5px; color: var(--ink); margin-top: 9px; }

  .label__body { padding: 8px 14px 0; font-family: "Griffy", cursive; color: var(--ink); }
  .ingredients { font-size: 10.5px; line-height: 13.5px; }
  .ingredients__head { display: block; }
  .label--short .label__body { padding: 8px 8px 0; }
  .label--short .ingredients { font-size: 7.6px; line-height: 10.3px; }

  .net-weight { position: absolute; left: 14px; bottom: 38px; font-family: "Griffy", cursive; font-size: 10.5px; color: var(--ink); }
  .label--short .net-weight { left: 20px; bottom: 6px; font-size: 7.5px; }

  .swatch { position: absolute; left: 38px; font-size: 12.5px; line-height: 15px; }
  .swatch__chip { width: 50px; height: 30px; margin-bottom: 6px; }
  .swatch--brown { top: 687px; color: var(--brown); }
  .swatch--navy { top: 786px; color: var(--navy); }
  .swatch--plum { top: 883px; color: var(--plum); }
  .swatch--brown .swatch__chip { background: var(--brown); }
  .swatch--navy .swatch__chip { background: var(--navy); }
  .swatch--plum .swatch__chip { background: var(--plum); }
</style>
</head>
<body>
<main class="sheet">
  <h1 class="sheet__title">Hair Shampoo</h1>

  <div class="size-caption" style="left:83px;top:88px">2'' x 4''</div>
  <div class="size-caption" style="left:323px;top:86px">2'' x 3''</div>
  <div class="size-caption" style="left:724px;top:86px">2'' x 4''</div>
  <div class="size-caption" style="left:964px;top:84px">2'' x 3''</div>
  <div class="size-caption" style="left:397px;top:542px">2'' x 4''</div>
  <div class="size-caption" style="left:637px;top:542px">2'' x 3''</div>

  <section class="label label--brown" style="left:83px;top:132px">
    <div class="label__top">
      <div class="brand">Soap Brambleton</div>
      <div class="foam foam--crest" role="img" aria-label="Illustrated soap bubbles"></div>
    </div>
    <div class="label__band"><div class="label__name">Hair Shampoo</div><div class="label__claim">100% Handmade - Sulfate Free</div></div>
    <div class="label__body"><p class="ingredients"><span class="ingredients__head">Ingredients:</span>Canola Oil, Ricinus Communis (Castor) Seed Oil, Cocos Nucifera (Coconut) Oil, Simmondsia Chinensis (Jojoba) Seed Oil, Aqua (Water), Potassium Hydroxide, Fragrance</p></div>
    <div class="net-weight">NT WT 8 oz</div>
    <div class="foam foam--base" role="img" aria-label="Illustrated soap bubbles"></div>
  </section>

  <section class="label label--short label--brown" style="left:323px;top:131px">
    <div class="label__top">
      <div class="brand">Soap Brambleton</div>
      <div class="foam foam--crest" role="img" aria-label="Illustrated soap bubbles"></div>
    </div>
    <div class="label__band"><div class="label__name">Hair Shampoo</div><div class="label__claim">100% Handmade &nbsp; Sulfate Free</div></div>
    <div class="label__body"><p class="ingredients"><span class="ingredients__head">Ingredients:</span>Canola Oil, Ricinus Communis (Castor) Seed Oil, Cocos Nucifera (Coconut) Oil, Simmondsia Chinensis (Jojoba) Seed Oil, Aqua (Water), Potassium Hydroxide, Fragrance</p></div>
    <div class="net-weight">NT WT &nbsp; 8 oz</div>
    <div class="foam foam--base" role="img" aria-label="Illustrated soap bubbles"></div>
  </section>

  <section class="label label--navy" style="left:724px;top:130px">
    <div class="label__top">
      <div class="brand">Soap Brambleton</div>
      <div class="foam foam--crest" role="img" aria-label="Illustrated soap bubbles"></div>
    </div>
    <div class="label__band"><div class="label__name">Hair Shampoo</div><div class="label__claim">100% Handmade - Sulfate Free</div></div>
    <div class="label__body"><p class="ingredients"><span class="ingredients__head">Ingredients:</span>Canola Oil, Ricinus Communis (Castor) Seed Oil, Cocos Nucifera (Coconut) Oil, Simmondsia Chinensis (Jojoba) Seed Oil, Aqua (Water), Potassium Hydroxide, Fragrance</p></div>
    <div class="net-weight">NT WT 8 oz</div>
    <div class="foam foam--base" role="img" aria-label="Illustrated soap bubbles"></div>
  </section>

  <section class="label label--short label--navy" style="left:964px;top:129px">
    <div class="label__top">
      <div class="brand">Soap Brambleton</div>
      <div class="foam foam--crest" role="img" aria-label="Illustrated soap bubbles"></div>
    </div>
    <div class="label__band"><div class="label__name">Hair Shampoo</div><div class="label__claim">100% Handmade &nbsp; Sulfate Free</div></div>
    <div class="label__body"><p class="ingredients"><span class="ingredients__head">Ingredients:</span>Canola Oil, Ricinus Communis (Castor) Seed Oil, Cocos Nucifera (Coconut) Oil, Simmondsia Chinensis (Jojoba) Seed Oil, Aqua (Water), Potassium Hydroxide, Fragrance</p></div>
    <div class="net-weight">NT WT &nbsp; 8 oz</div>
    <div class="foam foam--base" role="img" aria-label="Illustrated soap bubbles"></div>
  </section>

  <section class="label label--plum" style="left:397px;top:587px">
    <div class="label__top">
      <div class="brand">Soap Brambleton</div>
      <div class="foam foam--crest" role="img" aria-label="Illustrated soap bubbles"></div>
    </div>
    <div class="label__band"><div class="label__name">Hair Shampoo</div><div class="label__claim">100% Handmade - Sulfate Free</div></div>
    <div class="label__body"><p class="ingredients"><span class="ingredients__head">Ingredients:</span>Canola Oil, Ricinus Communis (Castor) Seed Oil, Cocos Nucifera (Coconut) Oil, Simmondsia Chinensis (Jojoba) Seed Oil, Aqua (Water), Potassium Hydroxide, Fragrance</p></div>
    <div class="net-weight">NT WT 8 oz</div>
    <div class="foam foam--base" role="img" aria-label="Illustrated soap bubbles"></div>
  </section>

  <section class="label label--short label--plum" style="left:637px;top:586px">
    <div class="label__top">
      <div class="brand">Soap Brambleton</div>
      <div class="foam foam--crest" role="img" aria-label="Illustrated soap bubbles"></div>
    </div>
    <div class="label__band"><div class="label__name">Hair Shampoo</div><div class="label__claim">100% Handmade &nbsp; Sulfate Free</div></div>
    <div class="label__body"><p class="ingredients"><span class="ingredients__head">Ingredients:</span>Canola Oil, Ricinus Communis (Castor) Seed Oil, Cocos Nucifera (Coconut) Oil, Simmondsia Chinensis (Jojoba) Seed Oil, Aqua (Water), Potassium Hydroxide, Fragrance</p></div>
    <div class="net-weight">NT WT &nbsp; 8 oz</div>
    <div class="foam foam--base" role="img" aria-label="Illustrated soap bubbles"></div>
  </section>

  <div class="swatch swatch--brown"><div class="swatch__chip"></div>CMYK<br>0 54 76 73 100</div>
  <div class="swatch swatch--navy"><div class="swatch__chip"></div>CMYK<br>100 100 0 50 100</div>
  <div class="swatch swatch--plum"><div class="swatch__chip"></div>CMYK<br>8 76 0 60 100</div>
</main>
</body>
</html>
```